Business Card Design

I need Business card designs with following on cards:

Dorian Felsk
Director

M: +61 491 208 356
D: +61 7 5580 1926
F: +61 7 5580 6471
E: dorian@mevrostrand.example.au

Mevro Group
Suite 4/61 North Calloway Road
Tindall Point QLD 4299

Ross Halvorn
Director

M: +61 438 902 615
D: +61 7 5580 1926
F: +61 7 5580 6471
E: ross@mevrostrand.example.au

Mevro Group
Tindall Point QLD 4299

Mevro Group Logo has been attached to brief.

Industry/Entity Type

Business

```html
<!DOCTYPE html>
<html lang="en">
<head>
<meta charset="utf-8">
<title>Mevro Group – Business Card</title>
<link rel="stylesheet" href="https://fonts.googleapis.com/css2?family=Comfortaa:wght@300;400&family=Marcellus&family=Saira+Condensed:wght@400;500&display=swap">
<style>
  :root {
    --backdrop: #8e0d0f;
    --card-black: #101010;
    --stripe-dark: #0b0b0b;
    --stripe-light: #1d1d1d;
    --glow: rgba(255, 255, 255, 0.16);
    --band-white: #f1f1f1;
    --ink-light: #f4f4f4;
    --ink-dark: #151515;
  }
  * { box-sizing: border-box; margin: 0; padding: 0; }
  html, body {
    width: 1200px;
    height: 960px;
    overflow: hidden;
  }
  body {
    background: var(--backdrop);
    position: relative;
  }
  .card {
    position: absolute;
    left: 250px;
    width: 700px;
    height: 400px;
    overflow: hidden;
    background:
      radial-gradient(ellipse 38% 60% at 45% 38%, var(--glow), transparent 70%),
      repeating-linear-gradient(90deg,
        var(--stripe-dark) 0px, var(--stripe-light) 38px,
        var(--stripe-dark) 76px),
      var(--card-black);
    box-shadow: 0 18px 40px rgba(0, 0, 0, 0.35);
  }
  .card--back { top: 50px; }
  .card--front { top: 500px; }

  .band {
    position: absolute;
    top: 0;
    bottom: 0;
    background: var(--band-white);
  }
  .card--back .band--left { left: 0; width: 62px; }
  .card--back .band--right { right: 0; width: 78px; }
  .card--front .band--right { right: 0; width: 86px; }

  .company-title {
    position: absolute;
    top: 66px;
    left: 62px;
    right: 78px;
    text-align: center;
    font-family: "Comfortaa", sans-serif;
    font-weight: 300;
    font-size: 40px;
    letter-spacing: 1px;
    color: var(--ink-light);
  }
  .address {
    position: absolute;
    top: 160px;
    left: 112px;
    font-family: "Comfortaa", sans-serif;
    font-weight: 300;
    font-size: 27px;
    line-height: 50px;
    color: var(--ink-light);
  }

  .person {
    position: absolute;
    top: 52px;
    left: 150px;
    width: 300px;
    text-align: center;
    font-family: "Marcellus", serif;
    font-size: 24px;
    line-height: 28px;
    color: var(--ink-light);
  }
  .contacts {
    position: absolute;
    top: 118px;
    left: 78px;
    list-style: none;
    font-family: "Saira Condensed", sans-serif;
    font-size: 24px;
    line-height: 30px;
    color: var(--ink-light);
  }
  .contacts li { margin-bottom: 34px; }

  .side-name {
    position: absolute;
    top: 0;
    bottom: 0;
    right: 0;
    width: 86px;
    display: flex;
    align-items: center;
    justify-content: center;
  }
  .side-name span {
    display: block;
    transform: rotate(90deg);
    white-space: nowrap;
    font-family: "Saira Condensed", sans-serif;
    font-weight: 500;
    font-size: 32px;
    letter-spacing: 1px;
    color: var(--ink-dark);
  }
</style>
</head>
<body>
  <section class="card card--back" aria-label="Card back">
    <div class="band band--left"></div>
    <div class="band band--right"></div>
    <h1 class="company-title">Mevro Group</h1>
    <p class="address">Suite 4/61 North Calloway Road<br>Tindall Point QLD 4299</p>
  </section>

  <section class="card card--front" aria-label="Card front">
    <div class="band band--right"></div>
    <p class="person">Dorian Felsk<br>Director</p>
    <ul class="contacts">
      <li>M: +61 491 208 356</li>
      <li>D: +61 7 5580 1926</li>
      <li>F: +61 7 5580 6471</li>
      <li>E: dorian@mevrostrand.example.au</li>
    </ul>
    <div class="side-name"><span>Mevro Group</span></div>
  </section>
</body>
</html>
```